Industrial Automation company requires a business card design

Valtrin Automation provides design & build of Automated Equipment for manufacturing industry.
www.valtrinautomation.example
The equipment we design is used for manufacturing in sectors such as medical device, pharmaceutical, aerospace and electronics.
We require a new business card design which incorporates our (New) logo and the key message words:
Automated Equipment:
Design, Build, Control, Test, Support

```html
<!DOCTYPE html>
<html lang="en">
<head>
<meta charset="utf-8">
<title>Valtrin Automation – Business Card</title>
<link href="https://fonts.googleapis.com/css2?family=Open+Sans:wght@400;600;700&display=swap" rel="stylesheet">
<style>
  :root {
    --backdrop: #2e2e2e;
    --card-white: #ffffff;
    --card-grey: #eeeeee;
    --brand-green: #0f7a3d;
    --ink: #222222;
    --band-dark: #2a2a2a;
    --white: #ffffff;
  }
  * { box-sizing: border-box; margin: 0; padding: 0; }
  html, body { width: 1200px; height: 848px; overflow: hidden; }
  body {
    background: var(--backdrop);
    font-family: "Open Sans", Arial, sans-serif;
    position: relative;
  }
  .card {
    position: absolute;
    left: 350px;
    width: 484px;
    height: 277px;
    border-radius: 17px;
    overflow: hidden;
  }
  .card-front {
    top: 128px;
    background: radial-gradient(ellipse at 50% 30%, var(--card-white) 40%, var(--card-grey) 100%);
  }
  .card-back {
    top: 444px;
    background: var(--brand-green);
  }
  .brand-name {
    position: absolute;
    font-weight: 700;
    letter-spacing: 1px;
    text-transform: uppercase;
    display: flex;
    align-items: center;
    gap: 8px;
    white-space: nowrap;
  }
  .brand-name .mark {
    border-radius: 50%;
    flex: none;
  }
  .card-front .brand-name { left: 36px; top: 56px; font-size: 21px; color: var(--brand-green); }
  .card-front .brand-name .mark { width: 22px; height: 22px; background: var(--brand-green); }
  .card-back .brand-name { right: 30px; top: 152px; font-size: 17px; color: var(--white); }
  .card-back .brand-name .mark { width: 18px; height: 18px; background: var(--white); }

  .holder-name {
    position: absolute; right: 40px; top: 152px;
    font-size: 13px; font-weight: 700; color: var(--brand-green);
  }
  .name-rule {
    position: absolute; left: 36px; top: 180px; width: 348px; height: 1px;
    background: var(--brand-green);
  }
  .holder-title {
    position: absolute; right: 40px; top: 172px;
    font-size: 11px; color: var(--ink);
  }
  .contact-list, .address {
    position: absolute; list-style: none; font-size: 10px; color: var(--ink);
  }
  .contact-list { left: 38px; top: 190px; }
  .address { left: 164px; top: 190px; }
  .contact-list li, .address li { height: 16px; line-height: 16px; display: flex; align-items: center; gap: 6px; }
  .address li.line { padding-left: 15px; }
  .icon { width: 9px; height: 9px; flex: none; fill: var(--brand-green); }
  .front-band { position: absolute; left: 0; bottom: 0; width: 484px; height: 16px; }

  .tagline {
    position: absolute; right: 55px; top: 226px;
    text-align: right; color: var(--white);
    font-size: 12.5px; font-weight: 700; line-height: 17px;
  }
</style>
</head>
<body>
  <section class="card card-front" aria-label="Card front">
    <div class="brand-name"><span class="mark"></span>Valtrin Automation</div>
    <div class="holder-name">DANIEL REED MORROW</div>
    <div class="holder-title">Chairman</div>
    <div class="name-rule"></div>
    <ul class="contact-list">
      <li><svg class="icon" viewBox="0 0 10 10"><path d="M2 0h2l1 2.5-1.3 1a6 6 0 0 0 2.8 2.8l1-1.3L10 6v2a2 2 0 0 1-2 2A8 8 0 0 1 0 2a2 2 0 0 1 2-2z"/></svg>(555) 014-2290</li>
      <li><svg class="icon" viewBox="0 0 10 10"><rect x="2.5" y="0" width="5" height="10" rx="1"/></svg>(555) 014-2291</li>
      <li><svg class="icon" viewBox="0 0 10 10"><circle cx="5" cy="5" r="4.2" fill="none" stroke="#0f7a3d" stroke-width="1.4"/><circle cx="5" cy="5" r="1.6"/></svg>sales@valtrin.example</li>
      <li><svg class="icon" viewBox="0 0 10 10"><circle cx="5" cy="5" r="5"/></svg>www.valtrinautomation.example</li>
    </ul>
    <ul class="address">
      <li><svg class="icon" viewBox="0 0 10 10"><path d="M5 0a3.5 3.5 0 0 1 3.5 3.5C8.5 6 5 10 5 10S1.5 6 1.5 3.5A3.5 3.5 0 0 1 5 0zm0 2a1.5 1.5 0 1 0 0 3 1.5 1.5 0 0 0 0-3z"/></svg>Norvane Technologies</li>
      <li class="line">2407 Alder Row</li>
      <li class="line">Brookfield, TX 70000</li>
    </ul>
    <svg class="front-band" viewBox="0 0 484 16" preserveAspectRatio="none" aria-hidden="true">
      <polygon points="0,0 308,0 300,16 0,16" fill="var(--band-dark)"/>
      <polygon points="312,0 484,0 484,16 304,16" fill="var(--brand-green)"/>
    </svg>
  </section>

  <section class="card card-back" aria-label="Card back">
    <div class="brand-name"><span class="mark"></span>Valtrin Automation</div>
    <p class="tagline">Automated Equipment:<br>Design, Build, Control, Test, Support</p>
  </section>
</body>
</html>
```